Meridian Path Advisors WordPress Site.

We need a modern, consultative looking, and exciting WordPress site to show case our new consulting company called Meridian Path Advisors LLC. Meridian Path Advisors (MPA) based in Southern California, provides expertise for companies who are interested in building an indirect sales channel. Some may think of this as building a Partner Program. Our offerings include, Discovery, Strategic Planning, Goals and Objective Setting, Partner Recruitment & Enablement, Team Building, and Outcome Definition. We purchased our logo from Loomgrove which is attached. The colors are Blue and Grey. The final design should convey a fresh, modern, and exciting look. Don't forget this is a consulting company, so we can't get too "wild". Hopefully we can come up with a nice balance. We attached our logo (two versions) and our Founder's photo. Please let us know what else you need to get started. I suspect you'll outline the design and we can iterate on the copy. Lastly, we'll be using Veltrahost as our hosting provider.

Target Market(s)

Small to mid-size SaaS Companies.

Industry/Entity Type

Consulting for Indirect Sales Channels

Coding

Coded - Design and coding required

Font styles to use
Other font styles liked:
• Please select a font that compliments the logo. Modern and easy to read.

Colors
0054AA
0677BA
7BADD7
CADEEF
E8F1F8
00AB8E
00BBA5
67D7C9
C6EFE9
E9F9F6
FFF300
FFF600
FEFA6F
FFFEC7
FFFEE8

Requirements
Must have
• My project must include the following pages. Homepage, About Us, Offerings & Services, and Contact Us
Nice to have
• Clean, bright and modern look. Area(s) and ability to insert video or blog posts.
Should not have
• Should not contain clutter. Black background.

```html
<!DOCTYPE html>
<html lang="en">
<head>
<meta charset="utf-8">
<title>Meridian Path Advisors</title>
<link href="https://fonts.googleapis.com/css2?family=Montserrat:wght@400;500;600;700&family=Roboto:wght@400;500&display=swap" rel="stylesheet">
<style>
:root{
  --blue:#0054AA;
  --blue-bright:#0677BA;
  --blue-card:#0a5fe0;
  --blue-deep:#0a3c9c;
  --grey:#9a9a9a;
  --grey-light:#efefef;
  --card:#eeeeee;
  --ink:#1b1b1b;
  --footer:#1c1c1c;
  --white:#ffffff;
}
*{margin:0;padding:0;box-sizing:border-box}
html,body{width:1200px;height:3516px;overflow:hidden;background:var(--white)}
body{font-family:'Montserrat',sans-serif;color:var(--ink);position:relative}
.abs{position:absolute}

/* header */
.topbar-item{position:absolute;top:14px;display:flex;align-items:center;gap:16px;font-size:19px;font-weight:500}
.round-icon{width:42px;height:42px;border-radius:50%;background:var(--blue);display:flex;align-items:center;justify-content:center}
.topbar-rule{position:absolute;top:67px;height:2px;background:#8a8a8a}
.nav a{position:absolute;top:86px;font-size:16px;font-weight:500;color:var(--ink);text-decoration:none}
.brand{position:absolute;left:474px;top:20px;width:222px;text-align:center}
.brand-dot{width:36px;height:36px;border-radius:50%;border:3px solid var(--blue);margin:0 auto 10px}
.brand-name{font-size:20px;font-weight:600;color:var(--blue);line-height:1.15}

/* hero */
.hero{position:absolute;left:0;top:142px;width:1200px;height:693px;overflow:hidden}
.hero-photo{position:absolute;inset:0;background:linear-gradient(100deg,#c9a87a 0%,#dcd6cc 35%,#e9eaec 60%,#b9c2cc 100%)}
.hero-circle{position:absolute;left:-1px;top:88px;width:520px;height:530px;border-radius:50%;background:#1c53a8;opacity:.96}
.hero-circle-full{position:absolute;left:0;top:88px;width:519px;height:530px;border-top-right-radius:265px;border-bottom-right-radius:265px;border-top-left-radius:0;border-bottom-left-radius:0;background:rgba(22,78,165,.95)}
.slider-dots{position:absolute;left:70px;top:228px;display:flex;flex-direction:column;gap:13px}
.slider-dots span{width:15px;height:15px;border-radius:50%;border:2px solid var(--white)}
.slider-dots span.on{background:var(--white)}
.hero h1{position:absolute;left:31px;top:337px;font-size:43px;font-weight:700;color:var(--white)}
.hero p{position:absolute;left:76px;top:410px;width:380px;font-size:18px;line-height:26px;color:var(--white)}
.btn{position:absolute;background:var(--grey);color:var(--white);border-radius:32px;display:flex;align-items:center;justify-content:center;font-weight:600}

/* story */
.story{position:absolute;left:0;top:835px;width:1200px;height:686px;background:linear-gradient(180deg,#0c6bd0 0%,#0a5ec0 55%,#1c4ea4 80%,#2a4c8c 100%)}
.section-title{position:absolute;left:0;width:1200px;display:flex;justify-content:center;align-items:center;gap:10px;font-weight:600}
.title-dot{width:26px;height:26px;border-radius:50%;border:3px solid currentColor}
.story .col{position:absolute;width:530px;color:var(--white);font-size:17.5px;line-height:25.5px}
.story b{font-weight:700;display:block}
.story .gap{height:25px}
.checks{position:absolute;top:308px;display:flex;flex-direction:column;gap:0;font-size:16px;line-height:25.5px;color:var(--white)}
.checks div{display:flex;align-items:center;gap:10px}
.story .mission{position:absolute;left:170px;top:462px;width:860px;text-align:center;color:var(--white);font-size:17.5px;line-height:26px}

/* services */
.card{position:absolute;top:1692px;width:237px;height:332px;background:var(--card);border-radius:14px;text-align:center}
.card.active{background:var(--blue-card);color:var(--white)}
.card .ring{width:100px;height:100px;margin:24px auto 0;border-radius:50%;border:5px solid var(--blue);background:var(--white);display:flex;align-items:center;justify-content:center}
.card h3{font-size:15.5px;font-weight:700;color:var(--blue);line-height:25px;margin-top:14px;padding:0 6px;min-height:50px}
.card.active h3{color:var(--white)}
.card p{font-size:14.5px;line-height:26px;margin-top:8px;padding:0 12px;color:#333}
.card.active p{color:var(--white)}
.card a{display:block;margin-top:14px;font-size:17px;font-weight:600;color:var(--blue);text-decoration:underline}
.card.active a{color:var(--white)}

/* testimonials */
.testi{position:absolute;left:0;top:2075px;width:1200px;height:536px}
.avatar{position:absolute;border-radius:50%;border:2px solid #333;background:linear-gradient(160deg,#9aa7b6,#5a6472)}
.testi-name{position:absolute;left:0;top:2318px;width:1200px;text-align:center;font-size:36px;font-weight:600}
.testi-text{position:absolute;left:140px;top:2370px;width:920px;text-align:center;font-size:16.5px;line-height:26px}
.testi-dots{position:absolute;top:2497px;left:537px;display:flex;gap:17px}
.testi-dots span{width:34px;height:4px;background:#111}
.testi-dots span.on{background:var(--blue-bright)}

/* contact */
.contact{position:absolute;left:0;top:2610px;width:1200px;height:486px;background:var(--blue-deep)}
.field{position:absolute;background:var(--white);border-radius:10px;font-family:'Roboto',sans-serif;font-size:14.5px;color:#444;padding:17px 17px}

/* footer */
.footer{position:absolute;left:0;top:3096px;width:1200px;height:420px;background:var(--footer);color:var(--white)}
.footer h4{position:absolute;font-size:22px;font-weight:600}
.footer .small{position:absolute;font-family:'Roboto',sans-serif;font-size:14px;line-height:23px}
.social{position:absolute;top:3329px;width:32px;height:32px;border-radius:50%;border:1.5px solid var(--white)}
</style>
</head>
<body>

<!-- Header -->
<header>
  <div class="topbar-item" style="left:99px">
    <div class="round-icon"><svg width="20" height="20" viewBox="0 0 24 24"><path fill="#fff" d="M6.6 10.8a15.1 15.1 0 0 0 6.6 6.6l2.2-2.2c.3-.3.7-.4 1-.2 1.1.4 2.3.6 3.6.6.6 0 1 .4 1 1V20c0 .6-.4 1-1 1A17 17 0 0 1 3 4c0-.6.4-1 1-1h3.5c.6 0 1 .4 1 1 0 1.3.2 2.5.6 3.6.1.3 0 .7-.2 1z"/></svg></div>
    <span>+ 1 888 888 8888</span>
  </div>
  <div class="topbar-rule" style="left:99px;width:351px"></div>
  <div class="topbar-item" style="left:714px">
    <div class="round-icon"><svg width="20" height="20" viewBox="0 0 24 24"><rect x="3" y="5" width="18" height="14" rx="2" fill="none" stroke="#fff" stroke-width="2"/><path d="M3 7l9 6 9-6" fill="none" stroke="#fff" stroke-width="2"/></svg></div>
    <span>info@meridianpathadvisors.com</span>
  </div>
  <div class="topbar-rule" style="left:714px;width:387px"></div>
  <nav class="nav">
    <a style="left:99px">Home</a>
    <a style="left:207px">About Us</a>
    <a style="left:339px">Our Story</a>
    <a style="left:734px">Testimonials</a>
    <a style="left:893px">Blog</a>
    <a style="left:990px">Contact Us</a>
  </nav>
  <div class="brand">
    <div class="brand-dot"></div>
    <div class="brand-name">Meridian Path Advisors</div>
  </div>
</header>

<!-- Hero -->
<section class="hero">
  <div class="hero-photo" role="img" aria-label="Photo of two business people working together at a laptop in a bright office"></div>
  <div class="hero-circle-full"></div>
  <div class="slider-dots"><span></span><span class="on"></span><span></span><span></span></div>
  <h1>Control Your Future.</h1>
  <p>Create. Optimize. Unleash the Power of Partnerships &amp; Alliances.</p>
  <div class="btn" style="left:159px;top:487px;width:195px;height:62px;font-size:20px">Get Started</div>
</section>

<!-- Our Story -->
<section class="story" role="img" aria-label="Blue tinted background photo of a pier over water">
  <div class="section-title" style="top:58px;color:var(--white);font-size:35px;font-weight:700"><span class="title-dot"></span>OUR STORY</div>
  <div class="col" style="left:97px;top:128px">
    <b>1.Do you worry about how you’re going to make your revenue number while managing costs?</b>
    You’re not alone. Most business leaders wrestle with the same concern.
    <div class="gap"></div>
    <b>2.What options do you have?</b>
    You can hire more salespeople and business development reps. You can invest in Searchly Ads, marketing campaigns, purchase lead lists, conduct webinars, increase social marketing, train your sales team, add solution engineers, etc. You get the picture...
  </div>
  <div class="col" style="left:651px;top:128px;width:460px">
    <b>3.Have you considered scaling your business through partnerships and alliances? Do you really know what that means?</b>
    Does your strategic plan include a robust indirect sales channel? If not, it should.
    <div class="gap"></div>
    <b>4.An indirect sales channel can open the door to...</b>
  </div>
  <div class="checks" style="left:649px">
    <div><svg width="15" height="15" viewBox="0 0 16 16"><circle cx="8" cy="8" r="8" fill="#fff"/><path d="M4.5 8.2l2.3 2.3 4.7-4.7" fill="none" stroke="#0a5ec0" stroke-width="2"/></svg>Lead generation</div>
    <div><svg width="15" height="15" viewBox="0 0 16 16"><circle cx="8" cy="8" r="8" fill="#fff"/><path d="M4.5 8.2l2.3 2.3 4.7-4.7" fill="none" stroke="#0a5ec0" stroke-width="2"/></svg>Deal acceleration</div>
    <div><svg width="15" height="15" viewBox="0 0 16 16"><circle cx="8" cy="8" r="8" fill="#fff"/><path d="M4.5 8.2l2.3 2.3 4.7-4.7" fill="none" stroke="#0a5ec0" stroke-width="2"/></svg>Higher close ratios</div>
    <div><svg width="15" height="15" viewBox="0 0 16 16"><circle cx="8" cy="8" r="8" fill="#fff"/><path d="M4.5 8.2l2.3 2.3 4.7-4.7" fill="none" stroke="#0a5ec0" stroke-width="2"/></svg>Cost management</div>
  </div>
  <div class="checks" style="left:877px">
    <div><svg width="15" height="15" viewBox="0 0 16 16"><circle cx="8" cy="8" r="8" fill="#fff"/><path d="M4.5 8.2l2.3 2.3 4.7-4.7" fill="none" stroke="#0a5ec0" stroke-width="2"/></svg>Improved margin</div>
    <div><svg width="15" height="15" viewBox="0 0 16 16"><circle cx="8" cy="8" r="8" fill="#fff"/><path d="M4.5 8.2l2.3 2.3 4.7-4.7" fill="none" stroke="#0a5ec0" stroke-width="2"/></svg>Scalability</div>
    <div><svg width="15" height="15" viewBox="0 0 16 16"><circle cx="8" cy="8" r="8" fill="#fff"/><path d="M4.5 8.2l2.3 2.3 4.7-4.7" fill="none" stroke="#0a5ec0" stroke-width="2"/></svg>Growth</div>
  </div>
  <p class="mission">Meridian Path Advisors can help you to think through the challenge and outline a plan that works for your company. Our mission is to help companies to control their future by leveraging an effective indirect sales channel.</p>
  <div class="btn" style="left:529px;top:574px;width:143px;height:52px;font-size:16px">Learn More</div>
</section>

<!-- Services -->
<section>
  <div class="section-title" style="top:1610px;color:var(--ink);font-size:26px;font-weight:500"><span class="title-dot" style="color:var(--blue)"></span>OUR SERVICES</div>
  <div class="card" style="left:98px">
    <div class="ring"><svg width="56" height="56" viewBox="0 0 56 56"><circle cx="32" cy="22" r="13" fill="none" stroke="#111" stroke-width="3"/><path d="M23 31L9 45" stroke="#111" stroke-width="5" stroke-linecap="round"/></svg></div>
    <h3>DISCOVERY</h3>
    <p>Lorem ipsum dolor sit amet, consectetur adipiscing elit, sed do eiusmod</p>
    <a>Read More</a>
  </div>
  <div class="card active" style="left:353px">
    <div class="ring"><svg width="56" height="56" viewBox="0 0 56 56"><circle cx="24" cy="20" r="9" fill="none" stroke="#111" stroke-width="2.5"/><circle cx="24" cy="20" r="3" fill="#111"/><circle cx="37" cy="13" r="5" fill="none" stroke="#111" stroke-width="2"/><path d="M8 42c8-6 14-6 22-2l14-6c3-1 4 3 1 4L30 46H8" fill="none" stroke="#111" stroke-width="2.5" stroke-linejoin="round"/></svg></div>
    <h3>STRATEGIC PLANNING</h3>
    <p>Lorem ipsum dolor sit amet, consectetur adipiscing elit, sed do eiusmod</p>
    <a>Read More</a>
  </div>
  <div class="card" style="left:609px">
    <div class="ring"><svg width="60" height="60" viewBox="0 0 60 60"><circle cx="30" cy="30" r="22" fill="none" stroke="#111" stroke-width="3"/><circle cx="30" cy="30" r="14" fill="none" stroke="#111" stroke-width="3"/><circle cx="30" cy="30" r="6" fill="none" stroke="#111" stroke-width="3"/><path d="M30 30L50 10" stroke="#111" stroke-width="3"/></svg></div>
    <h3>GOALS AND OBJECTIVE SETTING</h3>
    <p>Lorem ipsum dolor sit amet, consectetur adipiscing elit, sed do eiusmod</p>
    <a>Read More</a>
  </div>
  <div class="card" style="left:864px">
    <div class="ring"><svg width="56" height="56" viewBox="0 0 56 56"><rect x="18" y="8" width="28" height="38" rx="3" fill="none" stroke="#111" stroke-width="2.5"/><path d="M26 18h14M30 26h10M30 34h10" stroke="#111" stroke-width="2.5"/><circle cx="19" cy="32" r="8" fill="#fff" stroke="#111" stroke-width="2.5"/><path d="M13 38l-6 6" stroke="#111" stroke-width="3"/></svg></div>
    <h3>PARTNER RECRUITMENT &amp; ENABLEMENT</h3>
    <p>Lorem ipsum dolor sit amet, consectetur adipiscing elit, sed do eiusmod</p>
    <a>Read More</a>
  </div>
</section>

<!-- Testimonials -->
<section>
  <svg class="abs" style="left:0;top:2075px" width="1200" height="536" viewBox="0 0 1200 536">
    <path d="M0 128 Q600 -110 1200 152 V536 H0 Z" fill="var(--grey-light)"/>
    <path d="M0 128 Q600 -110 1200 152" fill="none" stroke="var(--blue)" stroke-width="3"/>
  </svg>
  <div class="section-title" style="top:2129px;color:var(--ink);font-size:26px;font-weight:500"><span class="title-dot" style="color:var(--blue)"></span>TESTIMONIALS</div>
  <div class="avatar" style="left:447px;top:2215px;width:62px;height:62px" role="img" aria-label="Client portrait"></div>
  <div class="avatar" style="left:500px;top:2208px;width:76px;height:76px" role="img" aria-label="Client portrait"></div>
  <div class="avatar" style="left:701px;top:2215px;width:58px;height:62px" role="img" aria-label="Client portrait"></div>
  <div class="avatar" style="left:640px;top:2208px;width:76px;height:76px" role="img" aria-label="Client portrait"></div>
  <div class="avatar" style="left:561px;top:2198px;width:96px;height:96px;border-color:#fff;border-width:4px" role="img" aria-label="Portrait of featured client"></div>
  <div class="testi-name">Elian Moss</div>
  <p class="testi-text">Lorem ipsum dolor sit amet, consectetur adipiscing elit, sed do eiusmod tempor incididunt ut labore et dolore magna aliqua. Ut enim ad minim veniam, quis nostrud exercitation ullamco laboris nisi ut aliquip ex ea commodo consequat. Duis aute irure dolor in reprehenderit in voluptate velit esse cillum dolore eu fugiat nulla pariatur. Excepteur sint occaecat cupidatat non proident, sunt in culpa qui officia deserunt mollit anim id est laborum."</p>
  <div class="testi-dots"><span class="on"></span><span></span><span></span></div>
</section>

<!-- Contact -->
<section class="contact">
  <div class="section-title" style="top:47px;color:var(--white);font-size:29px;font-weight:500"><span class="title-dot"></span>CONTACT US</div>
  <div class="field" style="left:309px;top:122px;width:282px;height:52px">First Name</div>
  <div class="field" style="left:609px;top:122px;width:282px;height:52px">Last Name</div>
  <div class="field" style="left:309px;top:187px;width:282px;height:52px">Email</div>
  <div class="field" style="left:609px;top:187px;width:282px;height:52px">Phone Number</div>
  <div class="field" style="left:309px;top:252px;width:578px;height:120px">Message</div>
  <div class="btn" style="left:529px;top:399px;width:143px;height:52px;font-size:16px">Submit Now</div>
</section>

<!-- Footer -->
<footer class="footer">
  <div class="abs" style="left:102px;top:87px;width:206px;text-align:center">
    <div class="brand-dot" style="width:50px;height:50px;border-color:#1a5fd0"></div>
    <div class="brand-name" style="color:#1a5fd0;font-size:20px">Meridian Path Advisors</div>
  </div>
  <h4 style="left:363px;top:55px">More Info</h4>
  <div class="small" style="left:363px;top:101px;line-height:30px">Terms &amp; Conditions<br>Privacy Policy<br>About Us<br>Support</div>
  <h4 style="left:561px;top:52px">Contact Us</h4>
  <div class="small" style="left:561px;top:101px;width:200px">ADDRESS<br>
    <svg width="9" height="12" viewBox="0 0 10 14"><path fill="#fff" d="M5 0a5 5 0 0 0-5 5c0 4 5 9 5 9s5-5 5-9a5 5 0 0 0-5-5zm0 7a2 2 0 1 1 0-4 2 2 0 0 1 0 4z"/></svg> Lorem ipsum dolor sit amet, consecteturs</div>
  <div class="small" style="left:561px;top:186px">PHONE<br>
    <svg width="12" height="12" viewBox="0 0 24 24"><path fill="#fff" d="M6.6 10.8a15.1 15.1 0 0 0 6.6 6.6l2.2-2.2c.3-.3.7-.4 1-.2 1.1.4 2.3.6 3.6.6.6 0 1 .4 1 1V20c0 .6-.4 1-1 1A17 17 0 0 1 3 4c0-.6.4-1 1-1h3.5c.6 0 1 .4 1 1 0 1.3.2 2.5.6 3.6.1.3 0 .7-.2 1z"/></svg> +1 888-888-8888</div>
  <div class="small" style="left:561px;top:245px;font-size:15px">EMAIL<br>
    <svg width="13" height="11" viewBox="0 0 24 20"><rect x="1" y="1" width="22" height="18" rx="2" fill="#fff"/><path d="M1 3l11 8 11-8" fill="none" stroke="#1c1c1c" stroke-width="2"/></svg> info@meridianpathadvisors .com</div>
  <h4 style="left:813px;top:55px">Newsletter</h4>
  <div class="small" style="left:813px;top:101px;width:290px">Lorem ipsum dolor sit amet, consectetur adipiscing elit, sed do eiusmod tempor</div>
  <div class="abs" style="left:810px;top:169px;width:276px;height:40px;background:#fff;border-radius:20px;color:#222;font-family:'Roboto',sans-serif;font-size:12.5px;padding:12px 19px">Enter Email
    <svg class="abs" style="right:17px;top:11px" width="19" height="19" viewBox="0 0 20 20"><circle cx="10" cy="10" r="10" fill="#111"/><path d="M5 10l10-5-3 11-2-4z" fill="#fff"/></svg>
  </div>
  <div class="abs" style="left:111px;top:323px;width:979px;height:1px;background:#777"></div>
  <div class="abs" style="left:0;top:356px;width:1200px;text-align:center;font-size:17px">© copyrights 2022 Meridian Path Advisors &nbsp;|&nbsp; All Rights Reserved</div>
</footer>
<div class="social" style="left:103px" role="img" aria-label="Professional network profile"></div>
<div class="social" style="left:140px" role="img" aria-label="Social page"></div>
<div class="social" style="left:177px" role="img" aria-label="Photo sharing profile"></div>

</body>
</html>
```